Business card and stationary designs for Harbor Summit Mentor
Harbor Summit Mentor
Business card and stationary designs for Harbor Summit Mentor - Consulting
Creative Brief
Professional
Reed Calloway
Executive & Professional Coach
4187 Willow Bend Lane Dallas TX 75231
RCalloway@harborsummitmentor.example
www.HarborSummitMentor.example
I want this to look clean, cutting edge, and for the design to stand out.
On the back of the business card I would like my logo and the phrase "Executive & Professional Coaching"

```html
<!DOCTYPE html>
<html lang="en">
<head>
<meta charset="utf-8">
<title>Harbor Summit Mentor – Business Card</title>
<link href="https://fonts.googleapis.com/css2?family=Cinzel:wght@500&family=Montserrat:wght@400;600&display=swap" rel="stylesheet">
<style>
  :root {
    --page-bg: #e4e4e2;
    --card-frost-top: #f4f4f3;
    --card-frost-bottom: #dcdcda;
    --band-dark: #3a3a3a;
    --band-darker: #2b2b2b;
    --ink-dark: #3b3b3b;
    --ink-light: #ffffff;
    --ink-soft: #d8d8d8;
    --divider: #9a9a9a;
  }
  * { margin: 0; padding: 0; box-sizing: border-box; }
  html, body {
    width: 1200px; height: 770px; overflow: hidden;
    background: var(--page-bg);
  }
  .card {
    position: absolute; left: 150px; top: 108px;
    width: 900px; height: 555px;
    border-radius: 18px; overflow: hidden;
    box-shadow: 0 14px 40px rgba(0,0,0,0.18);
  }
  .card-shapes { position: absolute; inset: 0; }
  .brand {
    position: absolute; left: 0; right: 0; top: 112px;
    display: flex; align-items: center; justify-content: center; gap: 18px;
  }
  .brand-mark {
    width: 14px; height: 14px; border-radius: 50%;
    background: var(--ink-dark);
  }
  .brand-name {
    font-family: 'Cinzel', serif; font-weight: 500;
    font-size: 44px; letter-spacing: 1px; color: var(--ink-dark);
  }
  .holder {
    position: absolute; left: 100px; top: 352px;
    font-family: 'Montserrat', sans-serif; color: var(--ink-light);
  }
  .holder-name { font-weight: 600; font-size: 24px; letter-spacing: 0.5px; }
  .holder-title { font-weight: 400; font-size: 19px; margin-top: 8px; color: var(--ink-soft); }
  .divider {
    position: absolute; left: 492px; top: 312px;
    width: 2px; height: 145px; background: var(--divider);
  }
  .contact-list {
    position: absolute; left: 520px; top: 310px;
    list-style: none;
    font-family: 'Montserrat', sans-serif; font-size: 15px; color: var(--ink-light);
  }
  .contact-item { display: flex; align-items: center; gap: 12px; height: 30px; }
  .contact-icon { width: 20px; height: 20px; flex: none; }
</style>
</head>
<body>
  <div class="card">
    <svg class="card-shapes" width="900" height="555" viewBox="0 0 900 555">
      <defs>
        <linearGradient id="frost" x1="0" y1="0" x2="0" y2="1">
          <stop offset="0" stop-color="var(--card-frost-top)"/>
          <stop offset="1" stop-color="var(--card-frost-bottom)"/>
        </linearGradient>
        <linearGradient id="band" x1="0" y1="0" x2="0" y2="1">
          <stop offset="0" stop-color="var(--band-dark)"/>
          <stop offset="1" stop-color="var(--band-darker)"/>
        </linearGradient>
      </defs>
      <rect class="card-frost" width="900" height="555" fill="url(#frost)"/>
      <path class="card-band" d="M0 228 C 250 268, 600 268, 900 208 L 900 478 C 600 505, 250 512, 0 470 Z" fill="url(#band)"/>
    </svg>

    <div class="brand">
      <span class="brand-mark"></span>
      <span class="brand-name">Harbor Summit Mentor</span>
    </div>

    <div class="holder">
      <div class="holder-name">REED CALLOWAY</div>
      <div class="holder-title">Managing Director</div>
    </div>

    <div class="divider"></div>

    <ul class="contact-list">
      <li class="contact-item">
        <svg class="contact-icon" viewBox="0 0 20 20"><circle cx="10" cy="10" r="10" fill="#fff"/><path d="M7 5.5l2 2-1.2 1.3c.7 1.4 1.8 2.5 3.2 3.2l1.3-1.2 2 2-1.3 1.7C9.5 14.3 5.7 10.5 5.5 7z" fill="#333"/></svg>
        <span>214 555 0186</span>
      </li>
      <li class="contact-item">
        <svg class="contact-icon" viewBox="0 0 20 20"><circle cx="10" cy="10" r="10" fill="#fff"/><path d="M7 5.5l2 2-1.2 1.3c.7 1.4 1.8 2.5 3.2 3.2l1.3-1.2 2 2-1.3 1.7C9.5 14.3 5.7 10.5 5.5 7z" fill="#333"/></svg>
        <span>214 555 0192</span>
      </li>
      <li class="contact-item">
        <svg class="contact-icon" viewBox="0 0 20 20"><circle cx="10" cy="10" r="10" fill="#fff"/><rect x="5" y="6.5" width="10" height="7" fill="none" stroke="#333" stroke-width="1.3"/><path d="M5 6.5l5 4 5-4" fill="none" stroke="#333" stroke-width="1.3"/></svg>
        <span>RCalloway@harborsummitmentor.example</span>
      </li>
      <li class="contact-item">
        <svg class="contact-icon" viewBox="0 0 20 20"><circle cx="10" cy="10" r="10" fill="#fff"/><circle cx="10" cy="10" r="5" fill="none" stroke="#333" stroke-width="1.2"/><ellipse cx="10" cy="10" rx="2.2" ry="5" fill="none" stroke="#333" stroke-width="1.1"/><path d="M5 10h10" stroke="#333" stroke-width="1.1"/></svg>
        <span>www.HarborSummitMentor.example</span>
      </li>
      <li class="contact-item">
        <svg class="contact-icon" viewBox="0 0 20 20"><circle cx="10" cy="10" r="10" fill="#fff"/><path d="M10 4.5a3.6 3.6 0 0 1 3.6 3.6c0 2.6-3.6 7-3.6 7s-3.6-4.4-3.6-7A3.6 3.6 0 0 1 10 4.5z" fill="#333"/><circle cx="10" cy="8.1" r="1.3" fill="#fff"/></svg>
        <span>4187 Willow Bend Lane Dallas TX 75231</span>
      </li>
    </ul>
  </div>
</body>
</html>
```